Tri-fold 8.5x11" brochure for my company's service

I am looking for a brochure design (to be used with Bramwell Mart printing service-- their templates have been included) for my company, Quillstone Scholastics. We host, support, and provide custom programming for the open-source product, Quillstone (which we also created).

I have included a Notes file, which provides more potential copy and points about the company. Please read it thoroughly, but feel free to experiment, edit, only use pieces of text, etc. Don't feel like you have to follow anything in there exactly.

I have included a couple different versions of our logo.

I have also included a zip file of several nice-looking screenshots from our software.

I have also included a zip file of stock photos I have purchased, but feel free to use other ones if you like-- You can use free watermarked versions and I will purchase the full image later and add it in. You also don't have to use the stock photos at all; your choice.

I can make my way around Gimp and Photoshop, so the final product MUST be in a format (with different image and text layers) I can edit myself later for final tweaks. I can work with psd and xcf (gimp) files. If you prefer to work with Illustrator or InDesign, please check google; there are several answers for how to convert to a layered psd file.

Final product must be in 300 DPI, per the printer's instructions. If you have to use lower-res versions of images (like for unpaid stock photos) that's OK as long as you give me the URL to buy to full version; I can place the full size images myself.

Target Market(s)

University / College faculty, registrars, administrators, VP's, presidents, etc.

Industry/Entity Type

Higher Education, Universities, Colleges, Student Success

Font styles to use
Serif
Sans Serif
Other font styles liked:
• MONTSERRAT is the font used in my logo, I use RALEWAY on the website. But these are not requirements-- Use what you think looks best.

Colors

Designer to choose colors to be used in the design.

Requirements
Must have
• The final product MUST be in a format (with different image and text layers) that I can edit myself later for final tweaks. I can work with psd and xcf (gimp) files. 300dpi required by printer. Follow the template files included for exact measurements. If you prefer to work with Illustrator or InDesign, please check google; there are several answers for how to convert to a layered psd file.
Nice to have
• I would like (if possible) to mention that the software, Quillstone is open source. I feel like that is a big selling point for universities. Also, please try to have a similar look and feel as the website: quillstonescholastics.example, if possible. If possible, you can mention that our service runs on state-of-the-art cloud based hardware, though this is not a requirement. Also, try to work in "affordable pricing" and/or "great for schools of all sizes", or similar, if possible. One of our selling points is that we are much less expensive than our competitors.
Should not have
• Big walls of text. I appreciate trying to cram in a lot of information from my notes, but too much and it can look very crowded.

```html
<!DOCTYPE html>
<html lang="en">
<head>
<meta charset="utf-8">
<title>Quillstone Scholastics – Tri-fold Brochure</title>
<link href="https://fonts.googleapis.com/css2?family=Montserrat:wght@400;500;700;800&display=swap" rel="stylesheet">
<style>
  :root {
    --page-bg: #e4e4e4;
    --cover-white: #ffffff;
    --ink: #2b2b2b;
    --accent-pink: #e4266f;
    --accent-orange: #f28414;
    --blue-deep: #0a6aa3;
    --blue-bright: #1590d2;
    --text-light: #eaf4fb;
    --text-muted: #b9d8ec;
    --photo-warm-a: #8a6a4c;
    --photo-warm-b: #c9a27a;
    --photo-cool-a: #f3f4f6;
    --photo-cool-b: #c8ccd3;
    --photo-crowd-a: #5b6f86;
    --photo-crowd-b: #b98f62;
  }
  * { box-sizing: border-box; margin: 0; padding: 0; }
  html, body { width: 1200px; height: 800px; overflow: hidden; }
  body {
    background: var(--page-bg);
    font-family: "Montserrat", sans-serif;
    display: flex; align-items: center; justify-content: center;
  }
  .brochure {
    width: 990px; height: 765px;
    display: grid; grid-template-columns: repeat(3, 1fr);
    box-shadow: 0 10px 30px rgba(0,0,0,.18);
  }
  .panel { padding: 34px 30px; display: flex; flex-direction: column; }

  /* Cover */
  .panel--cover { background: var(--cover-white); position: relative; overflow: hidden; }
  .brand { margin-top: 120px; display: flex; align-items: center; justify-content: center; gap: 12px; }
  .brand__mark { width: 20px; height: 20px; background: var(--blue-bright); flex: none; }
  .brand__name { font-weight: 700; font-size: 27px; line-height: 1.15; color: var(--ink); letter-spacing: .3px; }
  .cover-bands { position: absolute; left: 0; top: 330px; width: 100%; height: 300px; }
  .contact { margin-top: auto; position: relative; list-style: none; display: flex; flex-direction: column; gap: 9px; font-size: 13px; color: var(--ink); padding-left: 40px; }
  .contact li { display: flex; align-items: center; gap: 10px; }
  .contact svg { width: 18px; height: 18px; flex: none; }

  /* Inner panels */
  .panel--facts { background: var(--blue-deep); color: var(--text-light); justify-content: space-between; }
  .panel--features { background: var(--blue-bright); color: var(--text-light); justify-content: space-between; }
  .section-title {
    font-weight: 800; font-size: 19px; color: var(--text-muted);
    text-decoration: underline; text-underline-offset: 4px; text-decoration-thickness: 2px;
  }
  .panel--features .section-title { color: #ffffff; }
  .point { display: flex; gap: 8px; font-size: 13px; line-height: 1.35; }
  .point svg { width: 12px; height: 12px; flex: none; margin-top: 3px; }
  .point strong { display: block; font-weight: 700; font-size: 14px; color: var(--text-muted); }
  .panel--features .point strong { color: #ffffff; }
  .panel--facts .point { color: var(--text-muted); }
  .photo { height: 128px; border-radius: 44px; border: 2px solid rgba(255,255,255,.55); }
  .photo--advisors { background: linear-gradient(135deg, var(--photo-warm-b), var(--photo-warm-a)); }
  .photo--team { background: linear-gradient(135deg, var(--photo-warm-a), #3f4a58); }
  .photo--students { background: linear-gradient(135deg, var(--photo-crowd-b), var(--photo-crowd-a)); }
  .photo--office { background: linear-gradient(135deg, #b88a5f, #6f7f95); }
  .photo--whiteboard { background: linear-gradient(135deg, var(--photo-cool-a), var(--photo-cool-b)); }
  .feature-list { list-style: none; display: flex; flex-direction: column; gap: 5px; font-size: 11.5px; line-height: 1.35; }
  .feature-list li { display: flex; gap: 7px; }
  .feature-list svg { width: 10px; height: 10px; flex: none; margin-top: 3px; }
</style>
</head>
<body>
<svg width="0" height="0" style="position:absolute">
  <symbol id="arrow" viewBox="0 0 12 12"><path d="M1 6h8M6 2.5 9.5 6 6 9.5" fill="none" stroke="currentColor" stroke-width="2" stroke-linecap="round" stroke-linejoin="round"/></symbol>
</svg>

<main class="brochure">
  <section class="panel panel--cover">
    <div class="brand">
      <span class="brand__mark"></span>
      <span class="brand__name">Quillstone<br>Scholastics</span>
    </div>
    <svg class="cover-bands" viewBox="0 0 330 300" preserveAspectRatio="none" aria-hidden="true">
      <polygon points="0,90 330,20 330,62 0,132" fill="var(--accent-pink)"/>
      <polygon points="0,142 330,72 330,150 0,220" fill="var(--accent-orange)"/>
      <polygon points="0,230 330,160 330,210 0,280" fill="var(--blue-bright)"/>
    </svg>
    <ul class="contact">
      <li><svg viewBox="0 0 20 20"><circle cx="10" cy="10" r="8" fill="none" stroke="#2b2b2b" stroke-width="1.4"/><path d="M2 10h16M10 2c3 3 3 13 0 16M10 2c-3 3-3 13 0 16" fill="none" stroke="#2b2b2b" stroke-width="1.2"/></svg>quillstonescholastics.example</li>
      <li><svg viewBox="0 0 20 20"><circle cx="10" cy="10" r="8.5" fill="none" stroke="#2b2b2b" stroke-width="1.4"/><path d="M7 5.5c-1 .5-1.5 2 0 4.5s3.5 4 5 3.5l1-1.3-1.8-1.4-1 .8c-.8-.4-1.8-1.5-2.1-2.2l.8-1L7.6 6.6z" fill="#2b2b2b"/></svg>318-555-0147</li>
      <li><svg viewBox="0 0 20 20"><rect x="2" y="4.5" width="16" height="11" fill="none" stroke="#2b2b2b" stroke-width="1.4"/><path d="M2 4.5l8 6.5 8-6.5" fill="none" stroke="#2b2b2b" stroke-width="1.4"/></svg>info@quillstonescholastics.example</li>
    </ul>
  </section>

  <section class="panel panel--facts">
    <h2 class="section-title">FACTS ABOUT SERVICE</h2>
    <p class="point"><svg><use href="#arrow"/></svg><span>Quillstone is a powerful, open-source Student Success Management System.</span></p>
    <div class="photo photo--advisors" role="img" aria-label="Photo of an advisor helping a student at a desk"></div>
    <p class="point"><svg><use href="#arrow"/></svg><span><strong>Powerful</strong>Gain the full picture with early alerts, predictive analytics, and advanced advising</span></p>
    <div class="photo photo--team" role="img" aria-label="Photo of a team reviewing work together at a computer"></div>
    <p class="point"><svg><use href="#arrow"/></svg><span><strong>Flexible</strong>Quillstone easily adapts to your university, not the other way around</span></p>
    <div class="photo photo--students" role="img" aria-label="Photo of students sitting together with laptops"></div>
  </section>

  <section class="panel panel--features">
    <p class="point"><svg><use href="#arrow"/></svg><span><strong>Hassle-free</strong>Nothing to install on campus, and no need for additional IT team members</span></p>
    <div class="photo photo--office" role="img" aria-label="Photo of a staff member working at a desk in an office"></div>
    <p class="point"><svg><use href="#arrow"/></svg><span>We are happy to customize and custom program solutions to fit your needs</span></p>
    <div class="photo photo--whiteboard" role="img" aria-label="Photo of a person planning on a whiteboard"></div>
    <h2 class="section-title">TOP FEATURES</h2>
    <ul class="feature-list">
      <li><svg><use href="#arrow"/></svg>Advanced, yet easy-to-use advising and planning.</li>
      <li><svg><use href="#arrow"/></svg>Try out other degrees on the fly.</li>
      <li><svg><use href="#arrow"/></svg>AI-driven early alerts &amp; analytics for at-risk students.</li>
      <li><svg><use href="#arrow"/></svg>Send &amp; receive txt messages and emails, right from Quillstone.</li>
      <li><svg><use href="#arrow"/></svg>Easily integrates with existing systems on campus.</li>
      <li><svg><use href="#arrow"/></svg>Students can easily schedule advising sessions based on your availability</li>
    </ul>
  </section>
</main>
</body>
</html>
```